For lease banners for Businesses

I need to turn all of these banners into high quality graphics so I can get them printed on vinyl vertical banners that are 44"W x 88"H. So I need them most likely to be vector artwork, and ready to upload to a custom vinyl print shop.

```html
<!DOCTYPE html>
<html lang="en">
<head>
<meta charset="utf-8">
<title>For Lease Banner – Northgate Holdings</title>
<link rel="stylesheet" href="https://fonts.googleapis.com/css2?family=Anton&family=Montserrat:wght@500;700&family=Oswald:wght@600&family=Roboto+Condensed:wght@500&display=swap">
<style>
  :root {
    --backdrop: #adadad;
    --paper: #ffffff;
    --ink: #141414;
    --gold: #b98d3f;
    --sketch-light: #f6f6f6;
    --sketch-mid: #e4e4e4;
    --white: #ffffff;
  }
  * { box-sizing: border-box; margin: 0; padding: 0; }
  html, body {
    width: 1200px; height: 2323px; overflow: hidden;
    background: var(--backdrop);
  }
  .banner {
    position: absolute; left: 122px; top: 206px;
    width: 956px; height: 1911px;
    background: var(--paper);
    overflow: hidden;
  }
  .storefront-art {
    position: absolute; left: 0; top: 786px; width: 956px; height: 670px;
    background: linear-gradient(180deg, var(--paper) 0%, var(--sketch-light) 35%, var(--sketch-mid) 100%);
  }
  .headline {
    position: absolute; left: 116px; top: 94px;
    font-family: "Anton", sans-serif; font-weight: 400;
    font-size: 259px; line-height: 246px;
    color: var(--ink); letter-spacing: 6px;
    text-transform: uppercase;
  }
  .headline .line { display: block; height: 246px; white-space: nowrap; }
  .headline-dot {
    position: absolute; left: 629px; top: 772px;
    width: 45px; height: 45px; border-radius: 50%;
    background: var(--gold);
  }
  .headline-rule {
    position: absolute; left: 127px; top: 852px;
    width: 544px; height: 3px; background: var(--gold);
  }
  .use-list { position: absolute; left: 127px; top: 0; list-style: none; }
  .use-item {
    position: absolute; left: 0; width: 600px; height: 56px;
    display: flex; align-items: center;
  }
  .use-item svg { width: 56px; height: 56px; flex: none; }
  .use-item span {
    margin-left: 54px;
    font-family: "Montserrat", sans-serif; font-weight: 700;
    font-size: 34px; letter-spacing: 0.12em; color: var(--ink);
  }
  .info-band {
    position: absolute; left: 0; top: 1456px; width: 956px; height: 455px;
    background: var(--ink);
  }
  .brand {
    position: absolute; left: 172px; top: 40px; height: 128px;
    display: flex; align-items: center;
  }
  .brand-square { width: 120px; height: 128px; border: 3px solid var(--gold); }
  .brand-divider { width: 2px; height: 128px; background: var(--gold); margin-left: 31px; }
  .brand-name {
    margin-left: 34px;
    font-family: "Montserrat", sans-serif; font-weight: 500;
    color: var(--white); line-height: 1;
  }
  .brand-name .primary { display: block; font-size: 54px; letter-spacing: 0.12em; }
  .brand-name .secondary { display: block; font-size: 30px; letter-spacing: 0.42em; margin-top: 16px; }
  .band-rule {
    position: absolute; left: 87px; width: 782px; height: 3px; background: var(--gold);
  }
  .band-rule.top { top: 197px; }
  .band-rule.bottom { top: 308px; }
  .leasing-now {
    position: absolute; left: 88px; top: 208px;
    font-family: "Oswald", sans-serif; font-weight: 600;
    font-size: 66px; line-height: 88px; color: var(--gold);
    transform: scaleX(0.86); transform-origin: left center;
  }
  .contact-divider {
    position: absolute; left: 425px; top: 225px; width: 2px; height: 70px; background: var(--gold);
  }
  .contact { position: absolute; left: 454px; list-style: none; }
  .contact-line {
    position: absolute; left: 0; display: flex; align-items: center; white-space: nowrap;
    font-family: "Roboto Condensed", sans-serif; font-weight: 500; color: var(--white);
  }
  .contact-line svg { width: 34px; height: 30px; flex: none; }
  .contact-line span { margin-left: 19px; }
  .contact-line.phone { top: 217px; font-size: 32px; }
  .contact-line.email { top: 260px; font-size: 27px; }
  .space-types {
    position: absolute; left: 0; top: 332px; width: 956px; height: 56px;
    display: flex; justify-content: center; align-items: center; gap: 50px;
    font-family: "Roboto Condensed", sans-serif; font-weight: 500;
    font-size: 42px; color: var(--white); letter-spacing: 0.03em;
  }
  .space-types .sep { width: 14px; height: 14px; border-radius: 50%; background: var(--gold); }
</style>
</head>
<body>
  <main class="banner">
    <div class="storefront-art" role="img" aria-label="Line sketch of a glass-fronted restaurant and retail storefront with tables, chairs, plants and pendant lights"></div>

    <h1 class="headline">
      <span class="line">Your</span>
      <span class="line">Name</span>
      <span class="line">Here</span>
    </h1>
    <div class="headline-dot"></div>
    <div class="headline-rule"></div>

    <ul class="use-list">
      <li class="use-item" style="top:886px">
        <svg viewBox="0 0 56 56" fill="none" stroke="var(--gold)" stroke-width="2.5" stroke-linejoin="round"><path d="M6 20h44l-2 30H8z"/><path d="M19 24v-9a9 9 0 0 1 18 0v9"/></svg>
        <span>RETAIL</span>
      </li>
      <li class="use-item" style="top:955px">
        <svg viewBox="0 0 56 56" fill="none" stroke="var(--gold)" stroke-width="4" stroke-linecap="round"><path d="M12 46L40 16"/><circle cx="43" cy="12" r="6" stroke-width="3"/><path d="M44 46L16 16"/><path d="M10 6l10 10M6 10l10 10" stroke-width="3"/></svg>
        <span>RESTAURANT</span>
      </li>
      <li class="use-item" style="top:1024px">
        <svg viewBox="0 0 56 56" fill="none" stroke="var(--gold)" stroke-width="2.5" stroke-linejoin="round"><path d="M4 22h48l-6 26H10z"/><path d="M16 22l12-14 12 14"/><g fill="var(--gold)" stroke="none"><circle cx="18" cy="31" r="2.5"/><circle cx="28" cy="31" r="2.5"/><circle cx="38" cy="31" r="2.5"/><circle cx="20" cy="40" r="2.5"/><circle cx="28" cy="40" r="2.5"/><circle cx="36" cy="40" r="2.5"/></g></svg>
        <span>BOUTIQUE</span>
      </li>
      <li class="use-item" style="top:1094px">
        <svg viewBox="0 0 56 56" fill="none" stroke="var(--gold)" stroke-width="2.5" stroke-linecap="round"><path d="M10 24h32v8a14 14 0 0 1-28 0z"/><path d="M42 27h3a5 5 0 0 1 0 10h-5"/><path d="M4 50h46"/><path d="M21 8c-3 3 3 6 0 10M28 6c-3 3 3 6 0 12M35 8c-3 3 3 6 0 10"/></svg>
        <span>COFFEE</span>
      </li>
      <li class="use-item" style="top:1164px">
        <svg viewBox="0 0 56 56" fill="none" stroke="var(--gold)" stroke-width="2.5" stroke-linejoin="round"><rect x="4" y="16" width="48" height="32" rx="3"/><path d="M20 16v-6h16v6"/><path d="M4 28h48"/><rect x="24" y="24" width="8" height="8" fill="var(--paper)"/></svg>
        <span>OFFICE</span>
      </li>
    </ul>

    <section class="info-band">
      <div class="brand">
        <div class="brand-square"></div>
        <div class="brand-divider"></div>
        <div class="brand-name">
          <span class="primary">NORTHGATE</span>
          <span class="secondary">HOLDINGS</span>
        </div>
      </div>

      <div class="band-rule top"></div>
      <div class="leasing-now">LEASING NOW</div>
      <div class="contact-divider"></div>
      <ul class="contact">
        <li class="contact-line phone">
          <svg viewBox="0 0 34 30" fill="none" stroke="var(--gold)" stroke-width="2" stroke-linejoin="round"><path d="M9 2l5 6-3 4c2 4 5 7 9 9l4-3 6 5-3 5C15 28 4 17 4 6z"/></svg>
          <span>555-014-2290</span>
        </li>
        <li class="contact-line email">
          <svg viewBox="0 0 34 30" fill="none" stroke="var(--gold)" stroke-width="2" stroke-linejoin="round"><rect x="3" y="6" width="28" height="19"/><path d="M3 6l14 11 14-11M3 25l10-9M31 25l-10-9"/></svg>
          <span>leasing@northgateholdings.com</span>
        </li>
      </ul>
      <div class="band-rule bottom"></div>

      <div class="space-types">
        <span>RETAIL</span><span class="sep"></span>
        <span>RESTAURANT</span><span class="sep"></span>
        <span>OFFICE</span>
      </div>
    </section>
  </main>
</body>
</html>
```